Retractable Banner Design for Retail Shopping Event

I need a design for a 33” by 86” retractable banner. It should have my logo at the top (the largest element of the design) and the banner should also include my website and Instagram handle:
www.verikamode.com
@verikamode
I have included product pictures in the brief that can be used. I also included different versions of my logo file, including AI. I need the file to be ready to upload to my printer.
My store is an upscale women’s boutique. I am also attaching designs I have selected in the past to give an idea of my aesthetic.

```html
<!DOCTYPE html>
<html lang="en">
<head>
<meta charset="utf-8">
<title>Verikamode – Sip &amp; Shop Banner</title>
<link rel="stylesheet" href="https://fonts.googleapis.com/css2?family=Playfair+Display:wght@700;900&family=Mulish:wght@300;400&display=swap">
<style>
  :root {
    --slate: #56605d;
    --blush: #ecd0c8;
    --rose: #f3d8da;
    --pink-wash: #f6cfe0;
    --white: #ffffff;
    --gold: #d9b466;
    --sand: #e6d2bf;
    --text: #3f4644;
  }
  * { margin: 0; padding: 0; box-sizing: border-box; }
  html, body { width: 1200px; height: 3000px; overflow: hidden; background: var(--white); }
  .banner {
    position: relative;
    width: 1200px;
    height: 3000px;
    overflow: hidden;
    background:
      radial-gradient(ellipse 500px 300px at 95% 2%, rgba(246,207,224,.7), transparent 70%),
      radial-gradient(ellipse 420px 260px at 8% 3%, rgba(246,207,224,.45), transparent 70%),
      radial-gradient(ellipse 600px 500px at 10% 92%, rgba(246,190,215,.75), transparent 70%),
      radial-gradient(ellipse 500px 600px at 100% 75%, rgba(246,200,220,.6), transparent 70%),
      var(--white);
    font-family: "Mulish", sans-serif;
    color: var(--text);
  }
  .brand-name {
    position: absolute;
    left: 0; right: 0; top: 180px;
    text-align: center;
    font-family: "Playfair Display", serif;
    font-weight: 900;
    font-size: 132px;
    letter-spacing: 2px;
    color: var(--slate);
  }
  .earrings {
    position: absolute;
    left: 150px; top: 500px;
    width: 900px; height: 420px;
    background: radial-gradient(ellipse at 25% 50%, var(--gold) 0 22%, transparent 40%),
                radial-gradient(ellipse at 75% 50%, var(--gold) 0 22%, transparent 40%);
    opacity: .85;
  }
  .event-band {
    position: absolute;
    left: 0; top: 993px;
    width: 855px; height: 274px;
    background: var(--blush);
    display: flex; align-items: center;
    padding-left: 66px;
  }
  .event-title {
    font-family: "Playfair Display", serif;
    font-weight: 700;
    font-size: 138px;
    color: var(--slate);
    white-space: nowrap;
  }
  .product-row {
    position: absolute;
    left: 0; top: 1314px;
    width: 1200px; height: 490px;
    display: flex;
  }
  .product-tray {
    width: 594px; height: 100%;
    background: radial-gradient(ellipse 260px 180px at 50% 50%, #c9a36c 0 60%, #f8e7ea 62%);
  }
  .product-slippers {
    width: 606px; height: 100%;
    background: radial-gradient(ellipse 240px 170px at 55% 52%, #b9a8b8 0 40%, #ead9d6 55%, var(--rose) 75%);
  }
  .invite {
    position: absolute;
    left: 70px; top: 1905px;
    width: 500px;
  }
  .invite-heading {
    font-family: "Playfair Display", serif;
    font-weight: 700;
    font-size: 78px;
    color: var(--slate);
    line-height: 1.1;
  }
  .invite-sub {
    font-size: 56px;
    line-height: 1.45;
    color: var(--text);
  }
  .divider {
    position: absolute;
    left: 600px; top: 1900px;
    width: 6px; height: 245px;
    background: var(--blush);
  }
  .invite-detail {
    position: absolute;
    left: 680px; top: 1895px;
    width: 480px;
    font-size: 43px;
    line-height: 1.45;
    font-weight: 400;
    color: var(--text);
  }
  .product-bag {
    position: absolute;
    left: 81px; top: 2229px;
    width: 984px; height: 530px;
  }
  .footer {
    position: absolute;
    left: 0; top: 2798px;
    width: 1200px; height: 150px;
    display: flex;
  }
  .footer-web {
    width: 689px; height: 100%;
    background: var(--slate);
    color: var(--white);
    display: flex; align-items: center; justify-content: center;
    font-family: "Playfair Display", serif;
    font-weight: 700;
    font-size: 54px;
  }
  .footer-social {
    width: 511px; height: 100%;
    background: var(--blush);
    display: flex; align-items: center; justify-content: center; gap: 22px;
    font-family: "Playfair Display", serif;
    font-weight: 700;
    font-size: 54px;
    color: var(--slate);
  }
  .social-mark {
    width: 40px; height: 40px;
    border: 5px solid var(--slate);
    border-radius: 8px;
  }
</style>
</head>
<body>
  <main class="banner">
    <h1 class="brand-name">VERIKAMODE</h1>

    <div class="earrings" role="img" aria-label="Pair of gold beaded clover earrings with crystal centres"></div>

    <div class="event-band">
      <h2 class="event-title">Sip &amp; Shop</h2>
    </div>

    <section class="product-row">
      <div class="product-tray" role="img" aria-label="Round leopard print tray"></div>
      <div class="product-slippers" role="img" aria-label="Lavender slippers with fluffy pom-pom straps"></div>
    </section>

    <div class="invite">
      <p class="invite-heading">Come Enjoy</p>
      <p class="invite-sub">Sips,Snacks and Shopping!</p>
    </div>
    <div class="divider"></div>
    <p class="invite-detail">Be the first to preview our new winter collection and get an early start on your holiday gifting.</p>

    <svg class="product-bag" viewBox="0 0 984 530" role="img" aria-label="Nude leather tote bag with embroidered snake design">
      <defs>
        <linearGradient id="bagTone" x1="0" y1="0" x2="1" y2="1">
          <stop offset="0" stop-color="#e9d8c8"/>
          <stop offset="1" stop-color="#cdb39f"/>
        </linearGradient>
      </defs>
      <path d="M40 210 L870 170 L984 530 L0 530 Z" fill="url(#bagTone)"/>
    </svg>

    <footer class="footer">
      <div class="footer-web">www.verikamode.com</div>
      <div class="footer-social"><span class="social-mark"></span>@verikamode</div>
    </footer>
  </main>
</body>
</html>
```